Label design for unique cold brew coffee product

Require a label for front and back of a clear glass flint flask bottle. This will hold our speciality cold brew coffee. the label is to have your logo and represent our brand of being rustic, industrial, funky, mechanical etc as per our attached logo.

look forward to seeing the funky cool designs that will help bring our awesome product to market.

Target Market(s)

Hipsters, coffee connoisseurs, and one that enjoys a fine coffee.

Industry/Entity Type

Cafe

Requirements
Must have
• Brand recognition, staying true to the essence of what we are about, producing fine speciality cold brew coffee. Must have an rustic, industrial, funky, mechanical feel to be aligned with the logo.
• Please ensure the following is included and is editable on the label:
• Ingredients: Specialty Coffee & Filtered Water
• Brewed on :
• Keep Refrigerated
• Facebook, instagram etc logo
• Volume: 200ml etc
• Website: www.kettlewharf.com.au
• Origin of the coffee
Should not have
• no bright colours

```html
<!DOCTYPE html>
<html lang="en">
<head>
<meta charset="utf-8">
<title>Kettle Wharf Cold Brew – Label Set</title>
<link href="https://fonts.googleapis.com/css2?family=Oswald:wght@300;400;600&family=Open+Sans:wght@400&display=swap" rel="stylesheet">
<style>
  :root {
    --paper: #efefef;
    --kraft: #a8875b;
    --kraft-light: #b69668;
    --kraft-shade: #977548;
    --ink: #111111;
    --roast: #4a2a1c;
    --brand: #5a3222;
    --copy: #6e4e31;
    --accent-red: #c4262c;
    --stamp: #f2ece2;
  }
  * { margin: 0; padding: 0; box-sizing: border-box; }
  html, body { width: 1069px; height: 1200px; overflow: hidden; }
  body {
    background: var(--paper);
    position: relative;
    font-family: 'Oswald', sans-serif;
  }

  /* neck collars */
  .neck-label {
    position: absolute;
    top: 160px;
    width: 168px;
    height: 132px;
    background: linear-gradient(90deg, var(--kraft-shade), var(--kraft-light) 50%, var(--kraft-shade));
    display: flex;
    flex-direction: column;
    align-items: center;
    justify-content: center;
  }
  .neck-label--front { left: 218px; }
  .neck-label--back { left: 681px; }
  .cold-brew {
    font-weight: 600;
    font-size: 38px;
    line-height: 0.82;
    color: var(--brand);
    text-align: center;
    letter-spacing: -0.5px;
  }

  /* brand lockup */
  .brand {
    display: flex;
    flex-direction: column;
    align-items: center;
    gap: 6px;
  }
  .brand__mark {
    width: 22px;
    height: 22px;
    background: var(--brand);
  }
  .brand__name {
    font-family: 'Oswald', sans-serif;
    font-weight: 600;
    color: var(--brand);
    text-align: center;
    line-height: 1;
    letter-spacing: 2px;
  }
  .neck-label .brand__name { font-size: 20px; }

  /* body labels */
  .label {
    position: absolute;
    top: 511px;
    width: 339px;
    height: 438px;
    background: var(--kraft);
    overflow: hidden;
  }
  .label--front { left: 138px; }
  .label--back { left: 604px; }

  .ingredients-band {
    position: absolute;
    left: 0; top: 0;
    width: 100%;
    height: 40px;
    background: var(--ink);
    color: var(--kraft-light);
    font-weight: 300;
    font-size: 18px;
    letter-spacing: 0.2px;
    display: flex;
    align-items: center;
    justify-content: center;
  }

  .bean-art {
    position: absolute;
    left: 20px;
    top: 62px;
    width: 300px;
    height: 390px;
    border-radius: 48% 52% 44% 56%;
    background: radial-gradient(ellipse at 45% 45%, rgba(151,117,72,0.55), rgba(151,117,72,0.15) 70%, rgba(151,117,72,0));
    transform: rotate(-12deg);
  }

  .label--front .brand {
    position: absolute;
    left: 200px;
    top: 70px;
    width: 132px;
  }
  .label--front .brand__mark { width: 30px; height: 30px; }
  .label--front .brand__name { font-size: 28px; }

  .fridge-stamp {
    position: absolute;
    left: 30px;
    top: 92px;
    width: 150px;
    height: 62px;
    border: 3px solid var(--stamp);
    transform: rotate(-25deg);
    color: var(--stamp);
    padding: 4px 8px;
    display: flex;
    align-items: center;
    gap: 8px;
  }
  .fridge-stamp__words { line-height: 1; }
  .fridge-stamp__keep { font-weight: 600; font-size: 24px; letter-spacing: 1px; display: block; }
  .fridge-stamp__sub { font-weight: 400; font-size: 16px; display: block; }
  .fridge-stamp__temp { font-family: 'Open Sans', sans-serif; font-size: 9px; line-height: 1.2; }

  .origin {
    position: absolute;
    left: 108px;
    top: 198px;
    font-weight: 600;
    font-size: 78px;
    line-height: 0.94;
    color: var(--ink);
    letter-spacing: -1px;
  }
  .variety {
    position: absolute;
    left: 100px;
    top: 334px;
    font-weight: 400;
    font-size: 21px;
    color: var(--accent-red);
  }

  .socials {
    position: absolute;
    left: 48px;
    top: 396px;
    list-style: none;
    font-family: 'Open Sans', sans-serif;
    font-size: 10px;
    color: var(--roast);
  }
  .socials li { display: flex; align-items: center; gap: 5px; margin-bottom: 5px; }
  .socials__icon { width: 10px; height: 10px; background: var(--roast); border-radius: 2px; }

  .volume {
    position: absolute;
    left: 138px;
    top: 388px;
    width: 62px;
    height: 39px;
    background: var(--roast);
    color: var(--kraft-light);
    font-weight: 300;
    font-size: 17px;
    display: flex;
    align-items: center;
    justify-content: center;
  }
  .website {
    position: absolute;
    left: 210px;
    top: 403px;
    font-family: 'Open Sans', sans-serif;
    font-size: 9.5px;
    color: var(--roast);
  }

  .label--back .brand {
    position: absolute;
    left: 0;
    top: 36px;
    width: 100%;
  }
  .label--back .brand__name { font-size: 24px; }
  .origin-story {
    position: absolute;
    left: 30px;
    top: 157px;
    width: 279px;
    color: var(--copy);
    font-weight: 300;
    font-size: 12.2px;
    line-height: 1.43;
    text-transform: uppercase;
    text-align: center;
    letter-spacing: -0.3px;
  }
  .origin-story p + p { margin-top: 14px; }

  .view-caption {
    position: absolute;
    top: 1108px;
    font-weight: 600;
    font-size: 40px;
    color: var(--ink);
    width: 339px;
    text-align: center;
  }
  .view-caption--front { left: 138px; }
  .view-caption--back { left: 604px; }
</style>
</head>
<body>

  <div class="neck-label neck-label--front">
    <div class="brand">
      <span class="brand__mark"></span>
      <span class="brand__name">KETTLE<br>WHARF</span>
    </div>
  </div>

  <div class="neck-label neck-label--back">
    <div class="cold-brew">COLD<br>BREW</div>
  </div>

  <section class="label label--front">
    <div class="bean-art" role="img" aria-label="Faint engraved coffee bean illustration"></div>
    <div class="ingredients-band">SPECIALTY COFFEE &amp; FILTERED WATER</div>

    <div class="fridge-stamp">
      <div class="fridge-stamp__words">
        <span class="fridge-stamp__keep">KEEP</span>
        <span class="fridge-stamp__sub">refrigerated</span>
      </div>
      <div class="fridge-stamp__temp">+8°C<br>+2°C</div>
    </div>

    <div class="brand">
      <span class="brand__mark"></span>
      <span class="brand__name">KETTLE<br>WHARF</span>
    </div>

    <h1 class="origin">ACEH<br>GAYO</h1>
    <div class="variety">ARABICA COFFEE</div>

    <ul class="socials">
      <li><span class="socials__icon"></span>kettlewharf</li>
      <li><span class="socials__icon"></span>kettlewharf</li>
    </ul>
    <div class="volume">200ML</div>
    <div class="website">www.kettlewharf.com.au</div>
  </section>

  <section class="label label--back">
    <div class="brand">
      <span class="brand__mark"></span>
      <span class="brand__name">KETTLE<br>WHARF</span>
    </div>
    <div class="origin-story">
      <p>Coffee in Takengon or commonly called Aceh Gayo coffee is already famous in the world. As the name implies, this coffee is managed by Gayo people who are original residents of Takengon.</p>
      <p>Coffee Gayo type of Arabica has been certified Geography Indication (GI). Certificate of geographical indication is a sign showing the origin of a good because of geographical, natural, human, or combination. Thus, it produces certain characteristics and qualities in the goods produced (Article 1 PP RI No 51 Year 2007). And another great, Gayo coffee enjoyment has been recognized by the international.</p>
    </div>
  </section>

  <div class="view-caption view-caption--front">FRONT</div>
  <div class="view-caption view-caption--back">BACK</div>

</body>
</html>
```